New Design required for Disposable Gloves Pack

We need a new design for our range of disposable Gloves.
The brand name is "Marlow" I will attach the existing logo.

The needs to be 3 variations of the design (maybe different colours) that we can use for the different kinds of gloves: Latex Gloves, Clear Vinyl Gloves & Blue Vinyl Gloves.
Pack size is: 220x65x120mm.

Attached is a template to use showing all sides of the pack as flat. It is preferable that you supply an image of the complete folded pack as well with your design. Also attached is a PDF of our old pack design. Please use all the text on this old design for the new one.

The packs need to be easily differentiated from each other.

Target Market(s)

New Zealand Businesses, food processors & manufacturers. Medical & health care professionals

Font styles to use
Sans Serif

Requirements
Must have
• 3 variations of the same pack design to differentiate between the 3 types of gloves we offer: Latex Gloves, Clear Vinyl & Blue Vinyl Gloves.

```html
<!DOCTYPE html>
<html lang="en">
<head>
<meta charset="utf-8">
<title>Marlow Blue Vinyl Gloves – Pack Dieline</title>
<link rel="stylesheet" href="https://fonts.googleapis.com/css2?family=Outfit:wght@400;500;600&family=Tinos&display=swap">
<style>
  :root {
    --teal-deep: #175f68;
    --teal-light: #52ada6;
    --brand-green: #7ea63a;
    --paper: #ffffff;
    --ink: #1a1a1a;
    --dieline: #1d1d1d;
  }
  * { margin: 0; padding: 0; box-sizing: border-box; }
  html, body { width: 1200px; height: 1000px; overflow: hidden; background: var(--paper); }
  .canvas { position: relative; width: 1200px; height: 1000px; font-family: "Outfit", sans-serif; }
  .artwork { position: absolute; inset: 0; }
  .pack-size {
    position: absolute; left: 81px; top: 333px;
    font-family: "Tinos", serif; font-size: 15px; line-height: 23px; color: var(--ink);
  }
  .label { position: absolute; color: var(--paper); white-space: nowrap; }
  .product-name { font-size: 19px; font-weight: 600; }
  .contact { font-size: 11px; font-weight: 600; line-height: 15px; text-align: center; width: 200px; }
  .brand-name { font-size: 30px; font-weight: 500; letter-spacing: 2px; }
  .brand-name--top { left: 736px; top: 298px; color: var(--brand-green); }
  .brand-name--front { left: 362px; top: 585px; color: var(--paper); }
  .size-badge {
    position: absolute; left: 375px; top: 279px; width: 38px; height: 38px; border-radius: 50%;
    background: var(--teal-light); color: var(--paper);
    font-size: 20px; font-weight: 600; display: flex; align-items: center; justify-content: center;
  }
  .count { left: 793px; top: 500px; color: var(--teal-deep); font-size: 11px; font-weight: 600; line-height: 14px; }
  .features { left: 366px; top: 667px; font-size: 11px; font-weight: 500; display: flex; gap: 0; }
  .features li { list-style: none; }
  .features li::before { content: "\2713"; margin-right: 2px; }
  .features li:nth-child(1) { width: 67px; }
  .features li:nth-child(2) { width: 82px; }
  .features li:nth-child(3) { width: 109px; }
</style>
</head>
<body>
<div class="canvas">
  <svg class="artwork" width="1200" height="1000" viewBox="0 0 1200 1000">
    <defs>
      <clipPath id="pack-shape">
        <rect x="349" y="256" width="521" height="284"/>
        <rect x="66" y="540" width="1091" height="152"/>
      </clipPath>
    </defs>
    <g clip-path="url(#pack-shape)">
      <rect x="66" y="256" width="1091" height="436" fill="var(--teal-deep)"/>
      <!-- sweeping light band -->
      <path d="M440 256 C445 440 620 600 870 614 C990 620 1100 585 1157 538 L1157 256 Z" fill="var(--teal-light)"/>
      <!-- white top face -->
      <path d="M456 256 C468 420 560 515 608 540 L870 540 L870 256 Z" fill="var(--paper)"/>
      <!-- lower waves -->
      <path d="M66 648 C180 640 290 655 349 668 L349 692 L66 692 Z" fill="var(--teal-light)"/>
      <path d="M720 692 C820 650 1000 630 1157 638 L1157 692 Z" fill="var(--teal-deep)"/>
      <path d="M870 692 C960 682 1080 672 1157 668 L1157 692 Z" fill="var(--teal-light)"/>
      <path d="M66 588 C160 565 280 550 349 548 C480 545 560 570 650 610 C740 650 800 675 870 682 C960 690 1060 688 1157 690" fill="none" stroke="var(--paper)" stroke-width="1.4"/>
      <path d="M720 692 C820 650 1000 630 1157 638" fill="none" stroke="var(--paper)" stroke-width="1.4"/>
      <path d="M66 648 C180 640 290 655 349 668" fill="none" stroke="var(--paper)" stroke-width="1.2"/>
    </g>
    <!-- dispenser perforation -->
    <rect x="472" y="362" width="278" height="71" rx="16" fill="none" stroke="var(--teal-deep)" stroke-width="1.2" stroke-dasharray="4 3"/>
    <!-- glove icon placeholders -->
    <g role="img" aria-label="Glove pair icon">
      <circle cx="838" cy="494" r="18" fill="var(--teal-light)" stroke="var(--paper)" stroke-width="1.5"/>
    </g>
    <g role="img" aria-label="Glove pair icon">
      <circle cx="838" cy="578" r="18" fill="var(--teal-light)" stroke="var(--paper)" stroke-width="1.5"/>
    </g>
    <!-- dieline -->
    <g fill="none" stroke="var(--dieline)" stroke-width="1">
      <rect x="349.5" y="256.5" width="521" height="284"/>
      <rect x="66.5" y="540.5" width="1090" height="151"/>
      <line x1="349.5" y1="540" x2="349.5" y2="692"/>
      <line x1="870.5" y1="540" x2="870.5" y2="692"/>
    </g>
  </svg>

  <p class="pack-size">PACK SIZE<br>220 x 65 x 120mm</p>

  <div class="size-badge">L</div>
  <p class="label brand-name brand-name--top">Marlow</p>
  <p class="label product-name" style="left:368px; top:500px;">Blue Vinyl Gloves</p>
  <p class="label count">100<br>Gloves</p>

  <p class="label brand-name brand-name--front">Marlow</p>
  <ul class="label features">
    <li>Large</li><li>Single Use</li><li>Ambidexterous</li><li>Lightly Powered</li>
  </ul>

  <p class="label product-name" style="left:119px; top:596px;">Blue Vinyl Gloves</p>
  <p class="label contact" style="left:101px; top:654px;">0800 555 014<br>www.harbourpak.co.nz</p>

  <p class="label product-name" style="left:940px; top:596px;">Blue Vinyl Gloves</p>
  <p class="label contact" style="left:921px; top:654px;">0800 555 014<br>www.harbourpak.co.nz</p>
</div>
</body>
</html>
```